Business Card for a recruitment agency specializing in engineers and geeks.

I am looking to create Business Card Design for my company.
That
## Company name:
Quorvant Inc.
Quorvant is a term coined from the following concepts.
1. geek + engineer
2. geek utopia
## Company Description:
The concept of the company is to be a recruitment agency that creates a paradise for geeky engineers. We want to be a place where engineers can have more freedom and ideal career support.
# Target.
The noun itself is often given to companies that want to hire engineers, geeks, and IT-related personnel, so it would be nice to get the impression that this company seems to have good engineers and IT personnel. There are many occasions where I meet with the human resources department, president, or senior management and give it to them.
# Atmosphere
We are happy with simplicity, but with an impact that will help people remember the company. The logo is based on a dinosaur that does programming, so it should be somewhat playful, but since it will basically be used in a business setting, please don't make it too silly.
# About the logo
See the attached files. The company logo represents our engineers smiling upward because of our work, with the motif of a dinosaur doing programming.
## Color
We will leave the color scheme to you, but since the logo is in black and white, colors with such a taste would fit well.
## file format
ai, psd, png, svg
Industry/Entity Type
human resource and employment agency
Contact Information for Business Card
Company name, address, email, tel, URL,logo
Colors
Designer to choose colors to be used in the design.

```html
<!DOCTYPE html>
<html lang="en">
<head>
<meta charset="UTF-8">
<title>Quorvant Inc. — Business Card</title>
<link rel="stylesheet" href="https://fonts.googleapis.com/css2?family=Poppins:wght@400;600&display=swap">
<style>
  :root {
    --bg: #f2d94e;
    --card: #2f2f2f;
    --panel: #373737;
    --accent: #ecd036;
    --text: #ececec;
  }
  * { margin: 0; padding: 0; box-sizing: border-box; }
  html, body {
    width: 1200px; height: 1200px; overflow: hidden;
    background: var(--bg);
    font-family: "Poppins", sans-serif;
  }
  .canvas { position: relative; width: 1200px; height: 1200px; }
  .card {
    position: absolute; left: 323px; width: 555px; height: 317px;
    background: var(--card); border-radius: 16px; overflow: hidden;
    box-shadow: 0 12px 28px rgba(0,0,0,0.25);
  }
  .card--front { top: 261px; }
  .card--back { top: 621px; }

  /* front */
  .front__bar { position: absolute; left: 40px; top: 0; width: 11px; height: 107px; background: var(--accent); }
  .front__panel { position: absolute; left: 40px; top: 31px; width: 130px; height: 254px; background: var(--panel); }
  .front__web {
    position: absolute; left: 38px; top: 126px; width: 22px; height: 144px;
    writing-mode: vertical-rl; transform: rotate(180deg);
    color: var(--text); font-size: 14px; white-space: nowrap; text-align: left;
  }
  .front__name {
    position: absolute; left: 105px; top: 40px;
    color: var(--accent); font-weight: 600; font-size: 26px; letter-spacing: 0.2px; white-space: nowrap;
  }
  .front__role {
    position: absolute; left: 106px; top: 75px;
    color: var(--text); font-size: 15px; font-weight: 400; white-space: nowrap;
  }
  .front__brand {
    position: absolute; left: 106px; top: 154px;
    color: var(--accent); font-weight: 600; font-size: 15px;
  }
  .contact { position: absolute; left: 107px; display: flex; align-items: center; gap: 9px; color: var(--text); font-size: 14.5px; white-space: nowrap; }
  .contact svg { width: 15px; height: 15px; flex: none; }
  .contact--phone { top: 230px; }
  .contact--mail { top: 254px; }
  .front__address {
    position: absolute; left: 478px; top: 98px; width: 36px; height: 144px;
    writing-mode: vertical-rl; transform: rotate(180deg);
    color: var(--text); font-size: 12.5px; line-height: 17px; text-align: left; white-space: nowrap;
  }
  .front__pin { position: absolute; left: 482px; top: 254px; width: 30px; height: 20px; }

  /* back */
  .back__panel { position: absolute; left: 37px; top: 31px; width: 481px; height: 253px; background: var(--panel); }
  .back__bar { position: absolute; height: 11px; background: var(--accent); }
  .back__bar--top { left: 407px; top: 31px; width: 111px; }
  .back__bar--bottom { left: 37px; top: 273px; width: 110px; }
  .back__wordmark {
    position: absolute; left: 0; right: 0; top: 124px; text-align: center;
    color: var(--accent); font-weight: 600; font-size: 50px; line-height: 64px;
  }
</style>
</head>
<body>
<div class="canvas">
  <section class="card card--front">
    <div class="front__panel"></div>
    <div class="front__bar"></div>
    <p class="front__web">www.quorvant.com</p>
    <h1 class="front__name">DANIEL OKAFOR</h1>
    <p class="front__role">FOUNDER / CHIEF GEEK</p>
    <p class="front__brand">Quorvant</p>
    <p class="contact contact--phone">
      <svg viewBox="0 0 16 16" aria-hidden="true"><path fill="var(--accent)" d="M4 1.5l2.3 3-1.4 1.6a9 9 0 0 0 5 5l1.6-1.4 3 2.3-1.2 2.4C7.6 14.4 1.6 8.4 1.6 2.7z"/></svg>
      987 - 654 - 3210
    </p>
    <p class="contact contact--mail">
      <svg viewBox="0 0 16 16" aria-hidden="true"><rect x="1.5" y="3" width="13" height="10" rx="1" fill="none" stroke="var(--accent)" stroke-width="1.4"/><path d="M2 4l6 5 6-5" fill="none" stroke="var(--accent)" stroke-width="1.4"/></svg>
      daniel@quorvant.com
    </p>
    <p class="front__address">742 Harbor Lane, Fen<br>Town, NV 40218</p>
    <svg class="front__pin" viewBox="0 0 30 20" aria-hidden="true">
      <path d="M2 10a8 8 0 0 1 14-5.5L28 10 16 15.5A8 8 0 0 1 2 10z" fill="none" stroke="var(--accent)" stroke-width="1.3"/>
      <circle cx="10" cy="10" r="3.5" fill="none" stroke="var(--accent)" stroke-width="1.3"/>
    </svg>
  </section>

  <section class="card card--back">
    <div class="back__panel"></div>
    <div class="back__bar back__bar--top"></div>
    <div class="back__bar back__bar--bottom"></div>
    <p class="back__wordmark">Quorvant</p>
  </section>
</div>
</body>
</html>
```